Meridian 4.2

Book cover (14 x 20.5 cm) for a book: science fiction (futuristic) novel: Internet broke down, what happens to civilization? "Through a look, that of a physician of 2060, social and political developments are being described according to the changes in the relationship." Relationships to freedom, health, territories, mores, feminism, education and culture have changed radically. distance from the world, and then, one day, everything changes. Humanity is left in chaos, biological existence and relational life are immersed in what the world is like before the development of ... Unusual encounters, at the crossroads of several generations and communities of destinies, then
Target Market(s)
Adults
Industry/Entity Type
Book Publisher
Colors
Designer to choose colors to be used in the design.
Look and feel

```html
<!DOCTYPE html>
<html lang="fr">
<head>
<meta charset="utf-8">
<title>Meridian 4.2 — Corinne Valmont</title>
<link rel="stylesheet" href="https://fonts.googleapis.com/css2?family=Montserrat:wght@300;400&family=Roboto+Condensed:wght@700&family=Courier+Prime:wght@700&display=swap">
<style>
  :root {
    --concrete-light: #8a8a88;
    --concrete-mid: #6b6b69;
    --concrete-dark: #3a3a39;
    --concrete-deep: #242424;
    --data-glow: #35d6f5;
    --data-mid: #0c6f95;
    --data-deep: #02121c;
    --alert-red: #e40f0f;
    --ink-white: #ffffff;
  }
  * { margin: 0; padding: 0; box-sizing: border-box; }
  html, body { width: 819px; height: 1200px; overflow: hidden; background: var(--concrete-dark); }
  .cover {
    position: relative;
    width: 819px;
    height: 1200px;
    overflow: hidden;
    background:
      linear-gradient(180deg, var(--concrete-dark) 0%, var(--concrete-mid) 18%, var(--concrete-mid) 28%, var(--concrete-deep) 30%, var(--concrete-dark) 62%, var(--concrete-mid) 72%, var(--concrete-light) 100%);
  }
  .wall {
    position: absolute;
    top: 300px;
    width: 96px;
    height: 520px;
    background: linear-gradient(180deg, var(--concrete-mid), var(--concrete-dark));
  }
  .wall--left { left: 0; }
  .wall--right { right: 0; }
  .data-corridor {
    position: absolute;
    left: 96px;
    top: 336px;
    width: 632px;
    height: 470px;
    background:
      radial-gradient(ellipse 18% 40% at 50% 38%, #bff6ff 0%, var(--data-glow) 30%, transparent 100%),
      linear-gradient(90deg, var(--data-deep) 0%, var(--data-mid) 25%, var(--data-glow) 48%, var(--data-glow) 52%, var(--data-mid) 75%, var(--data-deep) 100%);
    -webkit-mask-image: linear-gradient(180deg, #000 75%, transparent 100%);
            mask-image: linear-gradient(180deg, #000 75%, transparent 100%);
  }
  .author {
    position: absolute;
    top: 108px;
    left: 0;
    width: 100%;
    text-align: center;
    font-family: "Montserrat", sans-serif;
    font-weight: 400;
    font-size: 50px;
    letter-spacing: 0.5px;
    color: var(--ink-white);
  }
  .alert-icon {
    position: absolute;
    left: 374px;
    top: 538px;
    width: 72px;
    height: 72px;
  }
  .alert-label {
    position: absolute;
    left: 298px;
    top: 617px;
    width: 222px;
    height: 46px;
    background: var(--alert-red);
    color: var(--ink-white);
    font-family: "Courier Prime", monospace;
    font-weight: 700;
    font-size: 24px;
    line-height: 46px;
    text-align: center;
  }
  .title {
    position: absolute;
    top: 872px;
    left: 0;
    width: 100%;
    text-align: center;
    font-family: "Roboto Condensed", sans-serif;
    font-weight: 700;
    font-size: 126px;
    line-height: 1;
    color: var(--ink-white);
    text-shadow: 0 2px 6px rgba(0,0,0,0.35);
  }
  .publisher {
    position: absolute;
    top: 1106px;
    left: 0;
    width: 100%;
    text-align: center;
    font-family: "Montserrat", sans-serif;
    font-weight: 300;
    font-size: 35px;
    color: var(--ink-white);
  }
</style>
</head>
<body>
  <main class="cover">
    <div class="wall wall--left"></div>
    <div class="wall wall--right"></div>
    <div class="data-corridor" role="img" aria-label="Glowing blue digital corridor lined with walls of scrolling code, receding into a bright vanishing point"></div>

    <h2 class="author">CORINNE VALMONT</h2>

    <svg class="alert-icon" viewBox="0 0 72 72" aria-hidden="true">
      <circle cx="36" cy="36" r="35" fill="var(--alert-red)" stroke="#ffffff" stroke-width="1"/>
      <path d="M31 13 h10 l-2 30 h-6 z" fill="#ffffff"/>
      <circle cx="36" cy="53" r="5.5" fill="#ffffff"/>
    </svg>
    <div class="alert-label">System Error</div>

    <h1 class="title">MERIDIAN 4.2</h1>
    <p class="publisher">Editions Solstice</p>
  </main>
</body>
</html>
```